Business Card Design - R.T. Custom Cabinets Ltd.

Design a business card, including a new logo for a new company in Vancouver, British Columbia, Canada.

The logo must be available as a separate file.

The card should include all company information including:
R.T. Custom Cabinets Ltd.
2786 Larchmoor Crescent
Burnaby, B.C. V7K 2P9
Telehone: 604-XXX-XXXX
Fax: 604-XXX-XXXX
www.rtcustomcabinets.example

As well as individual contact information for employees:
Name
Position
Telephone
Email

The card must include a thoughtful message as well

Target Market(s)

Custom Cabinets

Industry/Entity Type

Business

Contact Information for Business Card

Important information on the front, thoughtful message on the back

Colors
fbed22
9bcb3c
0355a3
ec1f27

Requirements
Must have
• See project description
Nice to have
• images that showcase custom cabinets (european, modern and traditional) styles

```html
<!DOCTYPE html>
<html lang="en">
<head>
<meta charset="utf-8">
<title>R.T. Custom Cabinets Ltd. – Business Card</title>
<link href="https://fonts.googleapis.com/css2?family=Open+Sans:wght@400;600;700&display=swap" rel="stylesheet">
<style>
  :root {
    --bg: #e4e4e6;
    --card: #ffffff;
    --brand-red: #ec1f27;
    --brand-blue: #0355a3;
    --ink-grey: #555555;
    --on-red: #ffffff;
  }
  html, body {
    margin: 0;
    width: 1200px;
    height: 1200px;
    overflow: hidden;
    background: var(--bg);
    font-family: "Open Sans", Arial, sans-serif;
  }
  .canvas {
    position: relative;
    width: 1200px;
    height: 1200px;
  }
  .card {
    position: absolute;
    left: 180px;
    width: 840px;
    height: 480px;
    background: var(--card);
    box-shadow: 0 10px 30px rgba(0,0,0,0.12);
    overflow: hidden;
  }
  .card--front { top: 90px; }
  .card--back  { top: 630px; }
  .card > svg { position: absolute; inset: 0; }

  .wordmark {
    font-weight: 700;
    color: var(--brand-blue);
    letter-spacing: 0.01em;
    white-space: nowrap;
  }
  .card--front .wordmark {
    position: absolute;
    left: 56px;
    top: 46px;
    font-size: 30px;
  }
  .card--back .wordmark {
    position: absolute;
    left: 0; right: 0;
    top: 50%;
    transform: translateY(-50%);
    text-align: center;
    font-size: 44px;
  }

  .person {
    position: absolute;
    right: 60px;
    top: 238px;
    text-align: right;
  }
  .person__name {
    font-size: 32px;
    font-weight: 600;
    color: var(--brand-red);
    letter-spacing: 0.03em;
    line-height: 1.1;
  }
  .person__role {
    font-size: 17px;
    color: var(--ink-grey);
  }

  .contact {
    position: absolute;
    color: var(--on-red);
    font-size: 16px;
    line-height: 1.45;
    list-style: none;
    margin: 0;
    padding: 0;
  }
  .contact li { display: flex; align-items: center; gap: 10px; }
  .contact svg { width: 14px; height: 14px; flex: none; }
  .contact--lines { left: 40px; top: 222px; }
  .contact--lines .gap { margin-top: 12px; }
  .contact--address {
    left: 200px;
    top: 388px;
    padding-left: 16px;
    border-left: 1px solid rgba(255,255,255,0.55);
    white-space: nowrap;
  }
  .contact--address li { align-items: flex-start; }
  .contact--address svg { margin-top: 4px; }
</style>
</head>
<body>
<main class="canvas">

  <section class="card card--front" aria-label="Business card front">
    <svg viewBox="0 0 840 480" width="840" height="480" aria-hidden="true">
      <path d="M0,130 C160,90 300,118 402,243 C497,363 622,423 775,480 L700,480 C580,430 470,370 380,260 C280,140 150,110 0,150 Z" fill="var(--brand-blue)"/>
      <path d="M0,152 C150,112 280,142 380,262 C470,372 580,432 700,482 L0,482 Z" fill="var(--brand-red)" stroke="#ffffff" stroke-width="6"/>
    </svg>

    <div class="wordmark">R.T. Custom Cabinets Ltd.</div>

    <div class="person">
      <div class="person__name">JORDAN VALE</div>
      <div class="person__role">Director</div>
    </div>

    <ul class="contact contact--lines">
      <li><svg viewBox="0 0 14 14"><path d="M3 1 L5.5 1 L6.5 4 L5 5.2 C5.8 7 7 8.2 8.8 9 L10 7.5 L13 8.5 L13 11 C13 12 12 13 11 13 C5.5 13 1 8.5 1 3 C1 2 2 1 3 1Z" fill="#fff"/></svg>604-XXX-XXXX</li>
      <li><svg viewBox="0 0 14 14"><rect x="3" y="1" width="8" height="4" fill="#fff"/><rect x="1" y="6" width="12" height="6" rx="1" fill="#fff"/></svg>604-XXX-XXXX</li>
      <li class="gap"><svg viewBox="0 0 14 14"><rect x="1" y="3" width="12" height="8" fill="#fff"/><path d="M1 3 L7 8 L13 3" stroke="var(--brand-red)" fill="none"/></svg>jordan@rtcustomcabinets.example</li>
      <li><svg viewBox="0 0 14 14"><circle cx="7" cy="7" r="5.5" fill="none" stroke="#fff" stroke-width="1.5"/><path d="M1.5 7 H12.5 M7 1.5 C4 5 4 9 7 12.5 M7 1.5 C10 5 10 9 7 12.5" stroke="#fff" fill="none"/></svg>www.rtcustomcabinets.example</li>
    </ul>

    <ul class="contact contact--address">
      <li><svg viewBox="0 0 14 14"><path d="M7 1 L13 7 L11 7 L11 13 L3 13 L3 7 L1 7 Z" fill="#fff"/></svg>
        <span>2786 Larchmoor<br>Crescent, Burnaby, B.C. V7K 2P9</span></li>
    </ul>
  </section>

  <section class="card card--back" aria-label="Business card back">
    <div class="wordmark">R.T. Custom Cabinets Ltd.</div>
  </section>

</main>
</body>
</html>
```